Chartered Professional Accounting Firm Needs a Business Card Design

We need a card design for an accounting firm based in Toronto, Ontario. The firm name is Lorne Patek Professional Corporation. The owner of the firm is a chartered professional accountant and a certified general accountant. Services of the firm include 60% tax preparation and consulting and 40% financial statements for corporation year-end. We would like a modern design. The color could be black, white, gray, blue or other color to bring more confidence to clients. The logo of the firm should be included in the design. Thanks
Updates

Name: Lorne Patek, CPA, CGA Address: 47 Marrow Creek Rd. Richmond Hill, ON K7T 5P3 Telephone: (416) 555-0142 Fax:(416) 555-0187 Email: lorne@lornepatek.example

Industry/Entity Type

Accounting

```html
<!DOCTYPE html>
<html lang="en">
<head>
<meta charset="utf-8">
<title>Lorne Patek Professional Corporation — Business Card</title>
<link rel="stylesheet" href="https://fonts.googleapis.com/css2?family=Cormorant+SC:wght@500;600;700&display=swap">
<style>
  :root {
    --backdrop: #1c1c1e;
    --card: #ffffff;
    --navy: #2b2a7a;
    --navy-deep: #1d1c5c;
    --grey: #8f8f96;
    --grey-light: #c9c9ce;
    --ink: #2a2a33;
  }
  * { margin: 0; padding: 0; box-sizing: border-box; }
  html, body {
    width: 1200px; height: 900px; overflow: hidden;
    background: var(--backdrop);
  }
  .card {
    position: absolute; left: 150px; top: 193px;
    width: 900px; height: 514px;
    background: var(--card);
    font-family: "Cormorant SC", "Times New Roman", serif;
    color: var(--ink);
    overflow: hidden;
  }
  .brand {
    position: absolute; top: 54px; left: 0; width: 100%;
    display: flex; justify-content: center; align-items: flex-start; gap: 16px;
  }
  .brand-mark {
    width: 58px; height: 58px; background: var(--navy); margin-top: 4px;
  }
  .brand-text { display: flex; flex-direction: column; }
  .brand-name {
    font-weight: 700; color: var(--navy);
    font-size: 40px; line-height: 36px; letter-spacing: 1px;
  }
  .brand-name .sub { display: block; font-size: 17px; line-height: 20px; letter-spacing: 1.5px; }
  .brand-tagline {
    margin-top: 4px; font-size: 11px; line-height: 13px; font-weight: 600;
    color: var(--grey); letter-spacing: 1.2px;
  }
  .holder {
    position: absolute; left: 58px; top: 212px;
    font-size: 34px; font-weight: 600; color: var(--navy);
  }
  .holder .credentials { font-size: 26px; }
  .divider {
    position: absolute; left: 478px; top: 186px; width: 1px; height: 116px;
    background: var(--grey-light);
  }
  .contact {
    position: absolute; left: 500px; top: 190px;
    list-style: none; font-size: 17px; font-weight: 600; line-height: 34px;
    color: var(--ink); letter-spacing: 0.6px;
  }
  .band { position: absolute; left: 0; bottom: 0; width: 900px; height: 170px; }
  .address {
    position: absolute; left: 0; bottom: 30px; width: 100%;
    text-align: center; color: #ffffff;
    font-size: 17px; font-weight: 600; letter-spacing: 1px;
  }
</style>
</head>
<body>
  <section class="card" aria-label="Business card for Lorne Patek, CPA, CGA">
    <header class="brand">
      <div class="brand-mark"></div>
      <div class="brand-text">
        <div class="brand-name">LORNE PATEK<span class="sub">PROFESSIONAL CORPORATION</span></div>
        <div class="brand-tagline">CHARTERED PROFESSIONAL ACCOUNTANT<br>CERTIFIED GENERAL ACCOUNTANT</div>
      </div>
    </header>

    <h1 class="holder">Lorne Patek, <span class="credentials">CPA, CGA</span></h1>
    <div class="divider"></div>
    <ul class="contact">
      <li>Telephone: (416) 555-0142</li>
      <li>Fax: (416) 555-0187</li>
      <li>Email: lorne@lornepatek.example</li>
    </ul>

    <svg class="band" viewBox="0 0 900 170" preserveAspectRatio="none" aria-hidden="true">
      <path d="M0 18 C 250 60, 560 78, 900 70 L 900 170 L 0 170 Z" fill="var(--grey-light)"/>
      <path d="M0 38 C 260 82, 560 96, 900 86 L 900 170 L 0 170 Z" fill="var(--navy)"/>
      <path d="M0 120 C 300 140, 600 150, 900 140 L 900 170 L 0 170 Z" fill="var(--navy-deep)" opacity="0.6"/>
    </svg>
    <p class="address">47 Marrow Creek Rd. Richmond Hill, ON K7T 5P3</p>
  </section>
</body>
</html>
```